Redesign of business card for Silverbrook Mechanical

We are looking for a new design for our business cards for Silverbrook Mechanical. We are a plumbing & HVAC construction company, operating on the West Coast of Canada and USA. Logo attached.
Industry/Entity Type
Construction - Plumbing & HVAC
Contact Information for Business Card
Name, address, phone numbers, email, website address
Look and feel

```html
<!DOCTYPE html>
<html lang="en">
<head>
<meta charset="utf-8">
<title>Silverbrook Mechanical – Business Card</title>
<link rel="stylesheet" href="https://fonts.googleapis.com/css2?family=Montserrat:wght@400;500;700&display=swap">
<style>
  :root {
    --backdrop: #8c8c8c;
    --card-light: #ffffff;
    --card-dark: #1c1c1c;
    --ink: #111111;
    --ink-soft: #6e6e6e;
    --silver: #c4c4c4;
    --rule: #222222;
  }
  * { margin: 0; padding: 0; box-sizing: border-box; }
  html, body {
    width: 1200px; height: 800px; overflow: hidden;
    background: var(--backdrop);
    font-family: "Montserrat", sans-serif;
  }
  .stage {
    position: relative; width: 1200px; height: 800px;
    display: flex; align-items: center; justify-content: center; gap: 40px;
  }
  .card {
    position: relative; width: 520px; height: 297px;
    border-radius: 22px; overflow: hidden;
  }
  .card--front { background: var(--card-light); color: var(--ink); }
  .card--back { background: var(--card-dark); display: flex; align-items: center; justify-content: center; }

  .brand {
    position: absolute; top: 38px; right: 32px;
    display: flex; align-items: center; gap: 10px;
    font-weight: 700; font-size: 17px; letter-spacing: 1.5px; text-transform: uppercase;
    color: var(--ink);
  }
  .brand__square { width: 14px; height: 14px; background: var(--ink); }

  .rule { position: absolute; height: 1px; background: var(--rule); }
  .rule--address { top: 112px; left: 290px; right: 32px; }
  .rule--person { top: 200px; left: 32px; width: 210px; }

  .address {
    position: absolute; top: 126px; right: 32px;
    text-align: right; font-size: 12.5px; line-height: 1.55; color: var(--ink-soft);
  }
  .address__label { color: var(--ink); font-weight: 500; }
  .address__block + .address__block { margin-top: 6px; }

  .person { position: absolute; top: 150px; left: 32px; }
  .person__name { font-weight: 700; font-size: 20px; letter-spacing: 0.5px; text-transform: uppercase; }
  .person__title { font-size: 13px; color: var(--ink-soft); margin-top: 2px; }

  .contacts {
    position: absolute; top: 212px; left: 32px; list-style: none;
    font-size: 12.5px; line-height: 1.5; color: var(--ink-soft);
  }
  .contacts li { display: flex; align-items: center; gap: 10px; }
  .contacts svg { width: 11px; height: 11px; fill: var(--ink); flex: none; }

  .back-brand {
    display: flex; align-items: center; gap: 14px;
    font-weight: 700; font-size: 26px; letter-spacing: 3px; text-transform: uppercase;
    color: var(--silver);
  }
  .back-brand__square { width: 22px; height: 22px; background: var(--silver); }
</style>
</head>
<body>
<main class="stage">
  <section class="card card--front" aria-label="Business card front">
    <div class="brand"><span class="brand__square"></span>Silverbrook Mechanical</div>
    <div class="rule rule--address"></div>
    <div class="address">
      <p class="address__block">2715 Canyon Crest Drive<br>Suite 140, Irvine, CA 92617</p>
      <p class="address__block"><span class="address__label">Mailing:</span> 8820 Lakeview Ave. S,<br>Suite #417 Seattle, WA 98178</p>
    </div>
    <div class="person">
      <p class="person__name">Daniel Harlow</p>
      <p class="person__title">President</p>
    </div>
    <div class="rule rule--person"></div>
    <ul class="contacts">
      <li><svg viewBox="0 0 24 24" aria-hidden="true"><path d="M6.6 10.8a15.1 15.1 0 0 0 6.6 6.6l2.2-2.2a1 1 0 0 1 1-.25 11.4 11.4 0 0 0 3.6.57 1 1 0 0 1 1 1V20a1 1 0 0 1-1 1A17 17 0 0 1 3 4a1 1 0 0 1 1-1h3.5a1 1 0 0 1 1 1c0 1.25.2 2.45.57 3.57a1 1 0 0 1-.25 1z"/></svg>1-866-555-0142 Toll Free</li>
      <li><svg viewBox="0 0 24 24" aria-hidden="true"><path d="M6.6 10.8a15.1 15.1 0 0 0 6.6 6.6l2.2-2.2a1 1 0 0 1 1-.25 11.4 11.4 0 0 0 3.6.57 1 1 0 0 1 1 1V20a1 1 0 0 1-1 1A17 17 0 0 1 3 4a1 1 0 0 1 1-1h3.5a1 1 0 0 1 1 1c0 1.25.2 2.45.57 3.57a1 1 0 0 1-.25 1z"/></svg>213-555-0187</li>
      <li><svg viewBox="0 0 24 24" aria-hidden="true"><path d="M2 5h20v14H2z M2 5l10 8 10-8" /></svg>info@silverbrookmech.com</li>
      <li><svg viewBox="0 0 24 24" aria-hidden="true"><path d="M12 2a10 10 0 1 0 0 20 10 10 0 0 0 0-20zm0 2c.9 1.2 1.7 3 2 5H10c.3-2 1.1-3.8 2-5zM4.3 11h3.7a17 17 0 0 0 .4 4H5a8 8 0 0 1-.7-4zm11.7 0h3.7a8 8 0 0 1-.7 4h-3.4a17 17 0 0 0 .4-4zm-6 0h4a15 15 0 0 1-.5 4h-3a15 15 0 0 1-.5-4z"/></svg>www.silverbrookmech.com</li>
    </ul>
  </section>

  <section class="card card--back" aria-label="Business card back">
    <div class="back-brand"><span class="back-brand__square"></span>Silverbrook Mechanical</div>
  </section>
</main>
</body>
</html>
```